Template für Gewinnspiel USB Stick
Zielgruppe
Gewinnspiel-Affine Personen
Aufgabenstellung
Gewünscht ist ein Template für eine Landing-Page eines Gewinnspiels.
Das Thema: Verlosung von 100 USB Sticks 16 GB unter allen Teilnehmern.
Das Layout soll Optisch ansprechend sein. Die Template können nach unten beliebig lang werden. (Inhalte aus der Datenbank)
Benötigte Seiten: Startseite, Datenschutz, Impressum, Gewinnspiel (Formular für das Gewinnspiel) und Teilnahmebedingungen.
Zur Orientierung:
http://brenner.kolbwerk.de/rollbahn
ist eine Seite mit unserem Gewinnspiel.
Klasse wären vielleicht auch Fotos.

```html
<!DOCTYPE html>
<html lang="de">
<head>
<meta charset="utf-8">
<title>Gewinnspiel – USB-Stick</title>
<link rel="stylesheet" href="https://fonts.googleapis.com/css2?family=Arimo:wght@400;700&family=Audiowide&display=swap">
<style>
  :root {
    --bg-deep: #040a1c;
    --bg-mid: #0b1f45;
    --panel: #07142e;
    --panel-border: #1d5d9e;
    --nav-top: #2a9fe0;
    --nav-bottom: #0d5fa8;
    --nav-text: #0a1a33;
    --orange: #ff7a10;
    --orange-dark: #e05a00;
    --cyan: #12a6e8;
    --cyan-light: #5fd4ff;
    --white: #ffffff;
    --body-text: #c9d6ea;
  }
  * { margin: 0; padding: 0; box-sizing: border-box; }
  html, body { width: 1200px; height: 906px; overflow: hidden; }
  body {
    position: relative;
    font-family: "Arimo", Arial, sans-serif;
    background:
      radial-gradient(ellipse 620px 420px at 600px 480px, var(--bg-mid), transparent 70%),
      var(--bg-deep);
  }
  .header-visual {
    position: absolute; left: 225px; top: 0; width: 360px; height: 285px;
    background: radial-gradient(ellipse 170px 110px at 190px 140px, #cfd6de 0%, #8d98a6 40%, #1b6fc0 70%, transparent 100%);
  }
  .header-swirl {
    position: absolute; left: 560px; top: 20px; width: 500px; height: 270px;
    background: radial-gradient(ellipse 260px 120px at 300px 150px, rgba(255,110,20,.35), rgba(30,110,200,.18) 60%, transparent 100%);
  }
  .claim { position: absolute; left: 507px; top: 78px; color: var(--white); font-weight: 700; font-size: 54px; line-height: 1; }
  .claim .claim-accent { color: var(--orange); font-size: 33px; margin-left: 8px; }
  .claim-product {
    position: absolute; left: 652px; top: 140px;
    font-family: "Audiowide", sans-serif; font-size: 60px; line-height: 1;
    color: var(--cyan-light); letter-spacing: 1px;
    text-shadow: 0 0 2px #0a3f80;
  }
  .page-panel {
    position: absolute; left: 166px; top: 274px; width: 863px; height: 574px;
    border: 1px solid var(--panel-border);
    background: linear-gradient(180deg, #0a1d3f 0%, var(--panel) 60%, #06112a 100%);
    overflow: hidden;
  }
  .main-nav {
    height: 70px;
    background: linear-gradient(180deg, var(--nav-top), var(--nav-bottom));
    position: relative;
  }
  .main-nav a {
    position: absolute; top: 0; height: 70px; line-height: 70px;
    font-size: 15px; font-weight: 700; color: var(--nav-text); text-decoration: none;
    transform: translateX(-50%); white-space: nowrap;
  }
  .main-nav a.is-active {
    left: 39px; width: 107px; height: 74px; transform: none; text-align: center;
    background: linear-gradient(180deg, #ff8a20, var(--orange-dark)); color: var(--white);
  }
  .headline { position: absolute; left: 41px; top: 104px; font-weight: 700; font-size: 42px; color: var(--cyan); white-space: nowrap; }
  .headline span { color: var(--orange); font-size: 36px; }
  .prize-visual {
    position: absolute; left: 44px; top: 183px; width: 218px; height: 113px;
    background: linear-gradient(135deg, #1b6fc0, #7cc8f2 50%, #1b6fc0);
    border-radius: 6px; opacity: .85;
  }
  .prize-count { position: absolute; left: 44px; top: 308px; width: 230px; text-align: center; color: var(--white); font-weight: 700; font-size: 25px; }
  .prize-note { position: absolute; left: 44px; top: 340px; width: 230px; text-align: center; color: var(--orange); font-weight: 700; font-size: 12px; }
  .intro-text { position: absolute; left: 302px; top: 186px; width: 482px; font-size: 11.5px; line-height: 20px; color: var(--body-text); }
  .promo-band {
    position: absolute; left: 0; top: 404px; width: 620px; height: 88px;
    background: linear-gradient(90deg, var(--orange) 0%, #ff8a20 55%, rgba(255,122,16,0) 100%);
  }
  .promo-band p { position: absolute; left: 29px; top: 28px; color: var(--white); font-weight: 700; font-size: 19px; white-space: nowrap; }
  .promo-band strong { font-size: 28px; }
  .promo-visual {
    position: absolute; left: 479px; top: 353px; width: 384px; height: 221px;
    background: radial-gradient(ellipse 180px 90px at 260px 100px, rgba(255,130,40,.9), rgba(240,190,160,.45) 55%, transparent 100%);
  }
</style>
</head>
<body>
  <div class="header-visual" role="img" aria-label="Silberner USB-Stick mit blauem Lichtschweif"></div>
  <div class="header-swirl" role="img" aria-label="Orange und blaue Lichtschwünge"></div>
  <h1 class="claim">GEWINNE<span class="claim-accent">jetzt einen</span></h1>
  <div class="claim-product">USB-STICK!</div>

  <main class="page-panel">
    <nav class="main-nav">
      <a class="is-active" href="#">Startseite</a>
      <a href="#" style="left:236px">Gewinnspiel</a>
      <a href="#" style="left:426px">Teilnahmebedingungen</a>
      <a href="#" style="left:612px">Datenschutz</a>
      <a href="#" style="left:754px">Impressum</a>
    </nav>

    <h2 class="headline">HEADLINE <span>- Subheadline</span></h2>

    <div class="prize-visual" role="img" aria-label="Vier blaue USB-Sticks"></div>
    <p class="prize-count">100 Stück</p>
    <p class="prize-note">zu gewinnen!</p>

    <p class="intro-text">Lorem ipsum dolor sit amet, consectetuer adipiscing elit. Aenean commodo ligula eget dolor. Aenean massa. Cum sociis natoque penatibus et magnis dis parturient montes, nascetur ridiculus mus. Donec quam felis, ultricies nec, pellentesque eu, pretium quis, sem. Nulla consequat massa quis enim. Donec pede justo, fringilla vel, aliquet nec, vulputate eget, arcu. In enim justo, rhoncus ut, imperdiet a, venenatis vitae, justo. Nullam dictum felis eu pede mollis pretium. ec quam felis, ultricies nec, pellentesque eu, pretium quis, sem. Nulla consequat massa quis enim. Donec pede justo, fringilla vel, aliquet nec, vulputate eget, arcu. In enim justo, rh</p>

    <div class="promo-band"><p><strong>16 Gigabyte</strong> für die Hosentasche!</p></div>
    <div class="promo-visual" role="img" aria-label="Hand hält orangefarbenen USB-Stick mit blauem Blitz"></div>
  </main>
</body>
</html>
```